Heritage Hollow Business Cards

Require a business card design. <br/><br/>Needs to include logo (either round or long version) plus these details:<br/>Maya Torvel<br/>Heritage Hollow<br/>maya@quonbrook.com.au<br/>02 6481 7390<br/>PO Box Glenwarra NSW 2913<br/>www.heritagehollow.com.au<br/><br/>I need in an editable format so that I can create for multiple staff members. <br/><br/>

Target Market(s)

We are an online store selling renovation products to home owners are builders. Looking for a classic classy design.

Industry/Entity Type

Home And Garden

Contact Information for Business Card

Maya Torvel
Heritage Hollow
maya@quonbrook.com.au
02 6481 7390
PO Box Glenwarra NSW 2913
www.heritagehollow.com.au

Colors

Designer to choose colors to be used in the design.

Requirements
Must have
• Must include Logo.

```html
<!DOCTYPE html>
<html lang="en">
<head>
<meta charset="utf-8">
<title>Heritage Hollow Business Cards</title>
<link href="https://fonts.googleapis.com/css2?family=Arimo:wght@400;700&display=swap" rel="stylesheet">
<style>
  :root {
    --backdrop: #0c0c0d;
    --card: #2a2a2c;
    --card-edge: #3a3a3d;
    --ink: #ececec;
    --ink-soft: #c9c9c9;
    --rule: #5a5a5d;
    --emboss: #3b3b3e;
  }
  * { margin: 0; padding: 0; box-sizing: border-box; }
  html, body { width: 1200px; height: 822px; overflow: hidden; }
  body {
    background: var(--backdrop);
    font-family: "Arimo", Arial, sans-serif;
    color: var(--ink);
  }
  .canvas {
    position: relative;
    width: 1200px;
    height: 822px;
    display: flex;
    align-items: center;
    justify-content: center;
    gap: 60px;
  }
  .card {
    width: 490px;
    height: 280px;
    background: var(--card);
    border: 1px solid var(--card-edge);
    border-radius: 3px;
    box-shadow: 0 18px 40px rgba(0,0,0,0.6);
    display: flex;
    flex-direction: column;
    align-items: center;
    justify-content: center;
    text-align: center;
  }
  .brand {
    display: flex;
    align-items: center;
    gap: 10px;
    font-weight: 400;
    font-size: 24px;
    color: var(--ink);
  }
  .brand-dot {
    width: 30px;
    height: 30px;
    border-radius: 50%;
    border: 1.5px solid currentColor;
  }
  .front .brand { margin-bottom: 26px; }
  .person-name {
    font-weight: 700;
    font-size: 19px;
    letter-spacing: 0.5px;
  }
  .rule {
    width: 110px;
    height: 1px;
    background: var(--rule);
    margin: 8px 0;
  }
  .company {
    font-weight: 700;
    font-size: 12px;
    letter-spacing: 0.3px;
  }
  .address {
    font-size: 13px;
    color: var(--ink-soft);
    margin-top: 3px;
  }
  .contact-line {
    font-size: 13px;
    color: var(--ink-soft);
  }
  .contact-line b, .web b { color: var(--ink); font-weight: 700; }
  .web {
    font-size: 13px;
    color: var(--ink-soft);
    margin-top: 4px;
  }
  .back .brand {
    font-size: 34px;
    color: var(--emboss);
    gap: 14px;
  }
  .back .brand-dot { width: 44px; height: 44px; border-width: 2px; }
</style>
</head>
<body>
  <main class="canvas">
    <section class="card front">
      <div class="brand"><span class="brand-dot"></span>Heritage Hollow</div>
      <h1 class="person-name">MAYA TORVEL</h1>
      <div class="rule"></div>
      <p class="company">HERITAGE HOLLOW</p>
      <p class="address">PO Box Glenwarra NSW 2913</p>
      <div class="rule"></div>
      <p class="contact-line"><b>P</b>: 02 6481 7390 | <b>E:</b> maya@quonbrook.com.au</p>
      <p class="web">www.<b>heritagehollow</b>.com.au</p>
    </section>
    <section class="card back">
      <div class="brand"><span class="brand-dot"></span>Heritage Hollow</div>
    </section>
  </main>
</body>
</html>
```